Company selling food supplements with CBD needs label.

We need a label design for a company called "VEX Lab ltd", is based in the UK, the market name is "VEX" or "VEX Velvet Ember Xtracts". The initial product is Virgin Organic Hemp Seed Oil with a CBD in a 10ml amber dropper bottle. The design should be simplicity and luxury. The design should include also box.

Target Market(s)

Food supplements on Pellmart UK

Industry/Entity Type

Supplement

Font styles to use
Other font styles liked:
• Some luxury

Colors

Designer to choose colors to be used in the design.

Requirements
Must have
• All the information on the label required by the UK for the food supplements, the same on the box. One version matt one transparent. The design should include different CBD content, one different bottle (250mg, 500mg, 750mg, 1000mg) .
• The label and box should include the following phrases: "DIRECTIONS: Food Supplement. Shake well before use. Use 4-6 drops 2-3 times a day. Leave the oil in your mouth for 30-60 seconds before swallowing. Gradually build up the dose to find your optimum dosage.
• CAUTION: Do not exceed the recommended daily intake. Do not use as a substitute for a varied diet. Do not use during pregnancy and breastfeeding. Store in a dark and cool place, away from sunlight. Keep away from children.
• INGREDIENTS: Hemp Seed Oil, Omega-6 (2800mg), Omega-3 (930mg), CBD (250mg)
• MANUFACTURED: VEX Lab Ltd, 87 Quillon Rd, Harrow, KT9 4PW, www,vexlabuk.co.uk, info@vexlabuk.co.uk.
• EXPIRED DATE: "
• The box should also include a place for bark code.
Nice to have
• Simple and elegant design vertical or horizontal with exposed company logo "VEX" or "VEX Velvet Ember Xtracts". The company logo is provided but designers may change it freely.
Should not have
• The best without pictures/graphics overloading simplicity and purity of design.

```html
<!DOCTYPE html>
<html lang="en">
<head>
<meta charset="utf-8">
<title>VEX Hemp Seed Oil with CBD – Label</title>
<link rel="stylesheet" href="https://fonts.googleapis.com/css2?family=Lato:ital,wght@0,400;0,700;0,900;1,700;1,900&family=Saira+Extra+Condensed:wght@500&display=swap">
<style>
  :root {
    --page-bg: #ececec;
    --label-bg: #232425;
    --brand-green: #10e81e;
    --ink-dark: #232425;
    --ink-light: #ffffff;
  }
  * { margin: 0; padding: 0; box-sizing: border-box; }
  html, body {
    width: 1200px; height: 697px; overflow: hidden;
    background: var(--page-bg);
  }
  .canvas { position: relative; width: 1200px; height: 697px; }
  .label {
    position: absolute; left: 40px; top: 69px;
    width: 1216px; height: 607px;
    transform: scale(0.921); transform-origin: 0 0;
    background: var(--label-bg);
    font-family: "Lato", sans-serif;
    overflow: hidden;
  }
  .label-shapes { position: absolute; inset: 0; width: 1216px; height: 607px; }
  .brand {
    position: absolute; left: 104px; top: 38px; width: 400px;
    text-align: center; color: var(--ink-dark);
  }
  .brand-name {
    font-weight: 900; font-size: 92px; line-height: 92px; letter-spacing: 4px;
  }
  .brand-tagline {
    font-family: "Saira Extra Condensed", sans-serif;
    font-weight: 500; font-size: 18px; letter-spacing: 1px; line-height: 20px;
    margin-top: -2px;
  }
  .product-title {
    position: absolute; left: 55px; width: 499px; text-align: center;
    color: var(--brand-green); font-weight: 900;
  }
  .product-qualifier { top: 251px; font-size: 40px; font-style: italic; font-weight: 700; letter-spacing: -0.5px; }
  .product-name { top: 305px; font-size: 58px; line-height: 60px; letter-spacing: -0.5px; }
  .product-volume {
    position: absolute; left: 204px; top: 522px; width: 200px; text-align: center;
    color: var(--ink-dark); font-weight: 900; font-size: 40px;
  }
  .info {
    position: absolute; left: 666px; top: 60px; width: 500px;
    color: var(--ink-light); font-size: 17.5px; line-height: 21px;
  }
  .info-block { margin-bottom: 16px; }
  .info-block + .info-block { margin-top: 0; }
  .info-heading { color: var(--brand-green); font-weight: 700; font-size: 17.5px; }
  .info-block--directions { margin-top: 18px; }
  .info-block--warnings { margin-top: 28px; }
  .info-block--maker { margin-top: 24px; }
</style>
</head>
<body>
<main class="canvas">
  <section class="label" aria-label="VEX Virgin Organic Hemp Seed Oil with CBD label">
    <svg class="label-shapes" viewBox="0 0 1216 607" aria-hidden="true">
      <path d="M22,0 L586,0 L530,110 Q500,170 440,170 L170,170 Q110,170 80,110 Z" fill="var(--brand-green)"/>
      <path d="M150,607 L190,540 Q205,515 235,515 L365,515 Q395,515 410,540 L458,607 Z" fill="var(--brand-green)"/>
      <g fill="none" stroke="var(--brand-green)" stroke-width="3">
        <path d="M112,272 L72,272 Q55,272 55,289 L55,391 Q55,408 72,408 L147,408"/>
        <path d="M495,272 L537,272 Q554,272 554,289 L554,391 Q554,408 537,408 L460,408"/>
      </g>
    </svg>

    <div class="brand">
      <div class="brand-name">VEX</div>
      <div class="brand-tagline">Velvet Ember Xtracts</div>
    </div>

    <div class="product-title product-qualifier">VIRGIN ORGANIC</div>
    <div class="product-title product-name">HEMP SEED OIL<br>WITH CBD</div>
    <div class="product-volume">10 ml</div>

    <div class="info">
      <div class="info-block">
        <div class="info-heading">INGREDIENTS:</div>
        <p>Lorem ipsum dolor sit amet, consectetuer adipiscing elit, sed diam nonummy nibh euismod tincidunt ut laoreet dolore magna aliquam erat volutpat. Ut wisi enim ad minim veniam, quis nostrud exerci tation ullamcorper suscipit lobortis nisl ut aliquip ex ea commodo consequat. Duis autem vel eum iriure dolor in hendrerit in vulputate velit esse molestie consequat, vel illum dolore eu feugiat</p>
      </div>
      <div class="info-block info-block--directions">
        <div class="info-heading">DIRECTIONS:</div>
        <p>Lorem ipsum dolor sit amet, consectetuer adipiscing elit, sed diam nonummy nibh euismod tincidunt ut laoreet dolore magna aliquam erat volutpat. Ut wisi enim ad.</p>
      </div>
      <div class="info-block info-block--warnings">
        <div class="info-heading">WARNINGS:</div>
        <p>Lorem ipsum dolor sit amet, consectetuer adipiscing elit, sed diam nonummy nibh euismod tincidunt ut laoreet dolore magna aliquam erat volutpat. Ut wisi enim ad.</p>
      </div>
      <div class="info-block info-block--maker">
        <div class="info-heading">MANUFACTURED AND DISTRIBUTED BY</div>
        <p>VEX VELVET EMBER XTRACTS<br>001 street, address VEX, UK<br>Email: hello@vexlabuk.co.uk | Ph: 000 0000 000</p>
      </div>
    </div>
  </section>
</main>
</body>
</html>
```